Modern and Improved business card design for Family Dental Practice

We have 2 sets of logo we have designed and now just need a business card layout and design for the office. Colors are on the logo. We can choose which logo we want to go with . The font can be changed to whatever seems modern and relevant. We are family dental office that has been open for over 15 years in South Austin Texas.

Target Market(s)

Handout Business cards to referrals and specialists

Industry/Entity Type

Dental

Contact Information for Business Card

We need address, phone, website and email address. 4870 North Loop Rd Suite 208 , Austin,Texas 78651....phone: 512-480-7319.....email- info@maplebrookdental-example.com....website - MapleBrookDental-example.com

Font styles to use
Serif
Decorative

Requirements
Must have
• my logo. We have 2 logos, but we can use just one or if we can incorporate one on one side and the other on the other side.
Nice to have
• Really just need a modern look and clean that incorporates the logo and colors .

```html
<!DOCTYPE html>
<html lang="en">
<head>
<meta charset="utf-8">
<title>Maple Brook Dental – Business Card</title>
<link href="https://fonts.googleapis.com/css2?family=Arimo:wght@400;700&display=swap" rel="stylesheet">
<style>
  :root {
    --bg: #c4c2bd;
    --green: #2b7d48;
    --green-deep: #1f6a3a;
    --leaf: #8fb04f;
    --white: #ffffff;
    --edge: #a9c060;
  }
  * { box-sizing: border-box; margin: 0; padding: 0; }
  html, body { width: 1200px; height: 857px; overflow: hidden; }
  body {
    background: var(--bg);
    font-family: "Arimo", Arial, sans-serif;
    position: relative;
  }
  .card {
    position: absolute;
    top: 280px;
    width: 520px;
    height: 297px;
    background: var(--green);
    border-bottom: 3px solid var(--edge);
    overflow: hidden;
  }
  .card--front { left: 55px; }
  .card--back { left: 625px; }

  .front-panel { position: absolute; inset: 0; }

  .brand {
    position: absolute;
    top: 96px;
    right: 34px;
    width: 220px;
    display: flex;
    align-items: center;
    gap: 10px;
    color: var(--green);
    font-weight: 700;
    font-size: 22px;
    line-height: 1.15;
  }
  .brand__dot {
    flex: none;
    width: 18px; height: 18px;
    border-radius: 50%;
    background: var(--leaf);
  }

  .edge-tab {
    position: absolute;
    left: 0; top: 176px;
    width: 14px; height: 14px;
    background: var(--leaf);
  }

  .contact {
    position: absolute;
    left: 42px;
    bottom: 30px;
    color: var(--white);
  }
  .contact__name { font-size: 16px; font-weight: 400; letter-spacing: 0.5px; text-transform: uppercase; }
  .contact__role { font-size: 11px; margin-top: 3px; }
  .contact__address { font-size: 11px; line-height: 1.45; margin-top: 12px; }
  .contact__list { list-style: none; margin-top: 12px; font-size: 11px; line-height: 1.6; }
  .contact__list li { display: flex; align-items: center; gap: 8px; }
  .icon { width: 9px; height: 9px; fill: var(--leaf); flex: none; }

  .back-brand {
    position: absolute;
    inset: 0;
    display: flex;
    align-items: center;
    justify-content: center;
    gap: 12px;
    color: var(--white);
    font-weight: 700;
    font-size: 26px;
  }
  .back-brand__dot { width: 20px; height: 20px; border-radius: 50%; background: var(--leaf); }
</style>
</head>
<body>

<section class="card card--front" aria-label="Business card front">
  <svg class="front-panel" viewBox="0 0 520 297" width="520" height="297" aria-hidden="true">
    <path d="M230 0 H520 V250 C470 262 400 250 345 218 C285 182 245 110 230 0 Z" fill="var(--white)"/>
  </svg>

  <div class="brand">
    <span class="brand__dot"></span>
    <span class="brand__name">Maple Brook Dental</span>
  </div>

  <span class="edge-tab"></span>

  <div class="contact">
    <p class="contact__name">Dana Whitfield</p>
    <p class="contact__role">Operational Manager</p>
    <p class="contact__address">4870 North Loop Rd Suite 208<br>Austin, Texas 78651</p>
    <ul class="contact__list">
      <li>
        <svg class="icon" viewBox="0 0 10 10"><path d="M2 0.5 L4 2.8 L3 4 C3.6 5.3 4.7 6.4 6 7 L7.2 6 L9.5 8 L8.3 9.5 C4 9 1 6 0.5 1.7 Z"/></svg>
        512-480-7319
      </li>
      <li>
        <svg class="icon" viewBox="0 0 10 10"><path d="M0 2 H10 V8.5 H0 Z M0 2 L5 5.5 L10 2" stroke="var(--green)" stroke-width="0.8"/></svg>
        info@maplebrookdental-example.com
      </li>
      <li>
        <svg class="icon" viewBox="0 0 10 10"><circle cx="5" cy="5" r="4.6"/><path d="M0.5 5 H9.5 M5 0.5 C2.5 3 2.5 7 5 9.5 M5 0.5 C7.5 3 7.5 7 5 9.5" stroke="var(--green)" stroke-width="0.7" fill="none"/></svg>
        MapleBrookDental-example.com
      </li>
    </ul>
  </div>
</section>

<section class="card card--back" aria-label="Business card back">
  <div class="back-brand">
    <span class="back-brand__dot"></span>
    <span>Maple Brook Dental</span>
  </div>
</section>

</body>
</html>
```